Service Menu refresh 2018 Update of menu pricing

We currently have service menus as attached. We will be updating our look via our homepage image, our service menu and our in-house beverage and treatment menu.
We are a natural and sustainable hair salon group and moving more towards head spa which consists of treatments, beauty, tanning as well as your traditional hair services. Our imagery needs to reflect our efforts in spa treatments in the hair and scalp area and use natural materials and colours reflecting sustainability.
Velin is the brand we stock and promote.

Target Market(s)

Men or women interesting in personal maintenance with natural and organic products and using sustainable practises

Industry/Entity Type

Hair And Beauty

Font styles to use
Sans Serif
Other font styles liked:
• Arial or Helvetica

Colors
9acb3c
abd037
cadf82
ffffff

Requirements
Must have
• Name on the front cover, locations on back cover
Nice to have
• Prestige feel, reflect male and female clients
Should not have
• Bold artificial writing or any type of cartoon images.
• Same images as existing menu.

```html
<!DOCTYPE html>
<html lang="en">
<head>
<meta charset="utf-8">
<title>Fernleaf Hair Salons – Service Menu</title>
<link rel="stylesheet" href="https://fonts.googleapis.com/css2?family=Lato:wght@300;400;700;900&display=swap">
<style>
  :root{
    --leaf:#9acb3c;
    --lime:#abd037;
    --pale:#cadf82;
    --white:#ffffff;
    --forest-dark:#08361a;
    --forest:#12562b;
    --forest-light:#1f7a3e;
    --ink:#0c3d1d;
    --black:#0b0d0b;
    --backdrop:#ebe6de;
  }
  *{box-sizing:border-box;margin:0;padding:0}
  html,body{width:1200px;height:823px;overflow:hidden}
  body{background:var(--backdrop);font-family:"Lato",Arial,sans-serif;color:var(--white);position:relative}

  .card{position:absolute;left:220px;width:760px;height:392px;overflow:hidden;
    background:radial-gradient(ellipse at 60% 40%,var(--forest-light) 0%,var(--forest) 45%,var(--forest-dark) 100%);
    box-shadow:0 6px 18px rgba(0,0,0,.18)}
  .card-front{top:12px}
  .card-back{top:419px}

  /* front */
  .brand-panel{position:absolute;left:0;top:0;width:330px;height:96px;background:var(--black);
    border-bottom-right-radius:30px;display:flex;align-items:center;gap:12px;padding-left:24px}
  .brand-dot{width:26px;height:26px;border-radius:50%;background:var(--leaf);flex:none}
  .brand-name{font-weight:300;font-size:25px;letter-spacing:.2px;color:var(--white)}
  .tagline{position:absolute;right:22px;top:20px;width:400px;text-align:right;font-weight:700;font-size:17px;line-height:1.25}
  .photo-ring{position:absolute;left:452px;top:78px;width:400px;height:400px;border-radius:50%;
    background:var(--forest-dark);padding:6px}
  .photo{width:100%;height:100%;border-radius:50%;
    background:radial-gradient(circle at 40% 40%,#f6efe9 0%,#e9d9cf 45%,#cfb6a8 75%,#6b4a3d 100%)}
  .locations{position:absolute;left:26px;top:112px;width:420px;list-style:none}
  .location{border-left:2px solid var(--lime);padding-left:9px;margin-bottom:7px;font-size:9.5px;line-height:1.22}
  .location-name{color:var(--lime);font-weight:900;font-size:10.5px;letter-spacing:.3px;text-transform:uppercase}

  /* back */
  .menu-block{position:absolute;top:16px}
  .menu-cut{left:20px}
  .menu-colour{left:392px}
  .price-grid{position:relative;display:grid;column-gap:5px}
  .menu-cut .price-grid{grid-template-columns:132px repeat(4,50px)}
  .menu-colour .price-grid{grid-template-columns:168px repeat(4,42px);column-gap:4px}
  .pill{position:absolute;top:-3px;bottom:-3px;border-radius:24px;border:1px solid var(--pale)}
  .pill.filled{background:var(--pale)}
  .price-grid > span{position:relative;font-size:9px;line-height:11.5px;height:11.5px;white-space:nowrap;text-align:center}
  .price-grid > span.label{text-align:left}
  .price-grid > .head-row{height:22px;line-height:22px;font-size:15px;font-weight:400;text-transform:uppercase;letter-spacing:.2px}
  .price-grid > .size{height:22px;line-height:22px;font-size:14px;font-weight:700}
  .price-grid > .sub{color:var(--lime);font-weight:900;text-transform:uppercase;font-size:9.5px}
  .menu-colour .label{text-transform:uppercase;font-size:8.5px}
  .on-fill{color:var(--ink)}
  .footnotes{margin-top:8px;font-size:8px;line-height:11px;color:var(--white);list-style:none}

  .pricing-note{position:absolute;left:0;right:0;top:330px;height:40px;background:var(--white);
    color:var(--forest);font-weight:700;font-size:9.5px;line-height:14px;text-align:center;padding-top:6px}
</style>
</head>
<body>

<section class="card card-front" aria-label="Menu front cover">
  <div class="brand-panel">
    <span class="brand-dot"></span>
    <span class="brand-name">Fernleaf Hair Salons</span>
  </div>
  <p class="tagline">Living a more natural and organic life is a philosophy not just a product certification</p>
  <div class="photo-ring">
    <div class="photo" role="img" aria-label="Photo of a woman with closed eyes receiving a relaxing scalp massage"></div>
  </div>
  <ul class="locations">
    <li class="location"><div class="location-name">Eastvale</div>Shop 104 Eastvale Centre, Harbour Rd, Eastvale<br>+61 (07) 3100 2001<br>eastvale@fernleafsalons.com.au</li>
    <li class="location"><div class="location-name">Northgate</div>Shop 22 Northgate Plaza, Wattle Road, Northgate<br>+61 (07) 3100 2002<br>northgate@fernleafsalons.com.au</li>
    <li class="location"><div class="location-name">Riverbend</div>Shop 308 Riverbend Mall, Ferry Rd, Riverbend<br>+61 (07) 3100 2003<br>riverbend@fernleafsalons.com.au</li>
    <li class="location"><div class="location-name">Lakeside</div>Shop 125 Lakeside Square, Harbour St, Lakeside<br>+61 (07) 3100 2004<br>lakeside@fernleafsalons.com.au</li>
    <li class="location"><div class="location-name">Riverside Womens Hospital</div>Banksia St, Riverside QLD 4000<br>+61 (07) 3100 2005<br>rwh@fernleafsalons.com.au</li>
  </ul>
</section>

<section class="card card-back" aria-label="Service menu prices">
  <div class="menu-block menu-cut">
    <div class="price-grid">
      <div class="pill" style="left:137px;width:50px"></div>
      <div class="pill filled" style="left:192px;width:50px"></div>
      <div class="pill" style="left:247px;width:50px"></div>
      <div class="pill filled" style="left:302px;width:50px"></div>

      <span class="label head-row">Cut &amp; Blowdry</span><span class="size">S</span><span class="size on-fill">M</span><span class="size">L</span><span class="size on-fill">XL</span>
      <span class="label sub">Ladies</span><span>$77</span><span class="on-fill">$88</span><span>$99</span><span class="on-fill">$110</span>
      <span class="label sub">Fringe</span><span></span><span></span><span></span><span></span>
      <span class="label">Trim</span><span>$25</span><span></span><span></span><span></span>
      <span class="label">Restyle</span><span>$35</span><span></span><span></span><span></span>
      <span class="label sub">Mens</span><span></span><span></span><span></span><span></span>
      <span class="label">Single clipper</span><span>$28</span><span></span><span></span><span></span>
      <span class="label">Style cut</span><span>$42</span><span></span><span></span><span></span>
      <span class="label sub">Children</span><span></span><span></span><span></span><span></span>
      <span class="label">10 and under</span><span>$24</span><span></span><span></span><span></span>
      <span class="label">11–16 Male</span><span>$32</span><span></span><span></span><span></span>
      <span class="label">11–16 Female</span><span>$48</span><span></span><span></span><span></span>
      <span class="label">add a wash</span><span>$7</span><span></span><span></span><span></span>
      <span class="label sub">Blowdry</span><span>$47</span><span class="on-fill">$57</span><span>$67</span><span class="on-fill">$77</span>
      <span class="label">Shampoo &amp; dry off</span><span>$25</span><span></span><span></span><span></span>
      <span class="label head-row">Treatments</span><span></span><span></span><span></span><span></span>
      <span class="label">deep treatment</span><span>$35</span><span></span><span></span><span></span>
      <span class="label">Head.Spa ritual</span><span>$65</span><span></span><span></span><span></span>
      <span class="label head-row">Upstyle</span><span></span><span></span><span></span><span></span>
      <span class="label">45 minutes</span><span>$105</span><span></span><span></span><span></span>
      <span class="label">60 minutes</span><span>$120</span><span></span><span></span><span></span>
    </div>
  </div>

  <div class="menu-block menu-colour">
    <div class="price-grid">
      <div class="pill" style="left:172px;width:42px"></div>
      <div class="pill filled" style="left:218px;width:42px"></div>
      <div class="pill" style="left:264px;width:42px"></div>
      <div class="pill filled" style="left:310px;width:42px"></div>

      <span class="label head-row">Colour</span><span class="size">S</span><span class="size on-fill">M</span><span class="size">L</span><span class="size on-fill">XL</span>
      <span class="label">Regrowth</span><span>$85</span><span class="on-fill">$145</span><span>$165</span><span class="on-fill">$185</span>
      <span class="label">Full colour tint</span><span>$125</span><span class="on-fill">$189</span><span>$209</span><span class="on-fill">$229</span>
      <span class="label">Regrowth lightening*</span><span>$165</span><span class="on-fill">$275</span><span>$375</span><span class="on-fill">$475</span>
      <span class="label">Balayage/Ombre*</span><span>$205</span><span class="on-fill">$255</span><span>$305</span><span class="on-fill">$355</span>
      <span class="label head-row">Leafdew</span><span></span><span></span><span></span><span></span>
      <span class="label">Regrowth</span><span>$99</span><span class="on-fill">$175</span><span>$195</span><span class="on-fill">$205</span>
      <span class="label">Full colour tint</span><span>$135</span><span class="on-fill">$155</span><span>$175</span><span class="on-fill">$195</span>
      <span class="label head-row">Foils*</span><span></span><span></span><span></span><span></span>
      <span class="label">Single*</span><span>$11</span><span class="on-fill">$13</span><span>$17</span><span class="on-fill">$22</span>
      <span class="label">1/4 Head</span><span>$135</span><span class="on-fill">$155</span><span>$175</span><span class="on-fill">$195</span>
      <span class="label">1/2 Head</span><span>$185</span><span class="on-fill">$235</span><span>$255</span><span class="on-fill">$265</span>
      <span class="label">Full Head</span><span>$225</span><span class="on-fill">$315</span><span>$335</span><span class="on-fill">$355</span>
      <span class="label head-row">Straight</span><span></span><span></span><span></span><span></span>
      <span class="label">Keratin straightening system</span><span>$365</span><span class="on-fill">$445</span><span>$535</span><span class="on-fill">$665</span>
    </div>
    <ul class="footnotes">
      <li>*Includes colour match &amp; toner</li>
      <li>*Minimum 6 foils without colour</li>
      <li>*Minimum charge on a Sunday is $4</li>
    </ul>
  </div>

  <p class="pricing-note">Pricing is indicative of average products used and time taken for each service. You will ALWAYS receive a firm price after your consultation.<br>S to the jaw line | M to the collarbone | L to the bra strap | XL past bra strap</p>
</section>

</body>
</html>
```